MEDITERRANEAN Cafe Website needed

We are a MEDITERRANEAN Café serving Coffee, breakfast, Pizza, Pasta, Sandwiches etc.

We need a home page, menu & venue, Reservations & Events, Delivery
Connect (Social media / Feedback / Contact us),Join our team
Updates

Can we keep the designs in Mediterranean colours, look, and feel pleasethanks Added Saturday, December 10, 2016

Project Deadline Extended Reason: I have guarantied the payment and upgraded the project. I would like this would to give more time for new designs to come in and a couple of potential designs to show more. Added Sunday, December 11, 2016

Industry/Entity Type

Cafe

Coding

Coded - Design and coding required

Number of Pages Required

5+ page

Requirements
Must have
• MEDITERRANEAN feel, colours, style etc.
• http://www.quillandfen (DOT) co (DOT) uk
Nice to have

```html
<!DOCTYPE html>
<html lang="en">
<head>
<meta charset="utf-8">
<title>Liora Cafe – Mediterranean Kitchen</title>
<link href="https://fonts.googleapis.com/css2?family=Fredoka:wght@500;600&family=Josefin+Sans:wght@300;400;600;700&family=Playball&display=swap" rel="stylesheet">
<style>
:root{
  --red:#f23d3b;
  --red-dark:#e23331;
  --cream:#f8eed6;
  --ink:#3b3b3b;
  --muted:#5a5a5a;
  --white:#ffffff;
}
*{margin:0;padding:0;box-sizing:border-box}
html,body{width:1200px;height:3087px;overflow:hidden}
body{background:var(--cream);font-family:'Josefin Sans',sans-serif;color:var(--ink);position:relative}
.btn{display:inline-block;background:var(--red);color:var(--white);font-family:'Josefin Sans',sans-serif;font-weight:700;font-size:12px;letter-spacing:.5px;text-transform:uppercase;text-decoration:none;text-align:center}

/* header */
.site-header{position:absolute;top:0;left:0;width:1200px;height:86px;background:#f4f1ec;display:flex;align-items:center;padding:0 40px}
.brand{display:flex;align-items:center;gap:8px;color:var(--red);font-weight:700;font-size:24px;text-decoration:none}
.brand-dot{width:22px;height:22px;border-radius:50%;background:var(--red)}
.main-nav{margin-left:auto;display:flex;gap:26px;font-size:12px;font-weight:600;text-transform:uppercase}
.main-nav a{color:var(--ink);text-decoration:none}
.main-nav a.active{color:var(--red)}
.btn-book{margin-left:54px;width:136px;height:46px;line-height:48px;font-size:12px}

/* hero */
.hero{position:absolute;top:86px;left:0;width:1200px;height:577px}
.hero-photo{position:absolute;inset:0;background:radial-gradient(ellipse at 55% 55%,#d8cf96 0%,#b9ad6a 30%,#e9e6e0 55%,#cfc9c1 75%,#6b4d3a 100%)}
.hero-copy{position:absolute;left:325px;top:159px;width:550px;text-align:center;color:var(--white)}
.hero-rule{height:1px;background:rgba(255,255,255,.75)}
.hero-title{font-family:'Fredoka',sans-serif;font-weight:600;font-size:46px;line-height:1;margin-top:26px;text-shadow:0 2px 6px rgba(0,0,0,.35)}
.hero-script{font-family:'Playball',cursive;font-size:56px;line-height:1.05;text-shadow:0 2px 6px rgba(0,0,0,.35)}
.hero-price{font-size:26px;font-weight:400;margin:4px 0 28px;text-shadow:0 2px 6px rgba(0,0,0,.35)}
.hero-price b{font-family:'Fredoka',sans-serif;font-size:46px;font-weight:600}
.hero .btn{position:absolute;left:532px;top:406px;width:137px;height:47px;line-height:49px}
.slider-dots{position:absolute;left:534px;top:537px;display:flex;gap:10px}
.slider-dots span{width:34px;height:4px;background:rgba(255,255,255,.45)}
.slider-dots span.on{background:var(--red)}

/* menu cards */
.menu-cards{position:absolute;top:786px;left:39px;display:flex;gap:19px}
.menu-card{width:361px;height:418px;background:var(--white);text-align:center}
.menu-card .photo{height:216px}
.menu-card h3{color:var(--red);font-weight:700;font-size:26px;margin-top:36px;text-transform:uppercase;letter-spacing:.5px}
.menu-card .price{font-size:18px;text-transform:uppercase;margin-top:6px}
.menu-card .price b{font-family:'Fredoka',sans-serif;font-size:30px;font-weight:600}
.menu-card .btn{width:136px;height:48px;line-height:50px;margin-top:24px}

/* ingredients */
.ingredients{position:absolute;top:1301px;left:0;width:1200px;height:562px;background:linear-gradient(100deg,#2a2826 0%,#3a3431 40%,#7a3a2a 62%,#3b3633 85%,#262423 100%);text-align:center;color:var(--white)}
.ingredients .script{font-family:'Playball',cursive;font-size:34px;padding-top:112px}
.ingredients h2{font-weight:700;font-size:44px;letter-spacing:1px;margin-top:2px}
.ingredients p{font-size:27px;font-weight:300;text-transform:uppercase;line-height:1.35;width:640px;margin:18px auto 0;letter-spacing:.5px}
.ingredients .btn{width:137px;height:47px;line-height:49px;margin-top:26px}

/* story */
.story{position:absolute;top:1986px;left:0;width:1200px}
.story-photo{position:absolute;top:0;height:443px}
.story-photo.marina{left:39px;width:266px;background:linear-gradient(180deg,#dfe7ec 0%,#b9c6b5 45%,#8c7a6e 100%)}
.story-photo.lounge{left:321px;width:266px;background:linear-gradient(180deg,#e8c98a 0%,#f1dfb8 45%,#c75a3e 80%,#a5482f 100%)}
.story-text{position:absolute;left:609px;top:0;width:552px}
.story-text .script{font-family:'Playball',cursive;color:var(--red);font-size:32px;line-height:1}
.story-text h2{font-family:'Fredoka',sans-serif;font-weight:500;font-size:46px;color:var(--ink);margin-top:6px}
.story-text p{font-size:12.5px;line-height:2.55;color:var(--muted);margin-top:14px}
.story-text p+p{margin-top:0}

/* follow */
.follow{position:absolute;top:2527px;left:0;width:1200px;height:221px;background:var(--red);text-align:center;color:var(--white)}
.follow h2{font-weight:600;font-size:28px;padding-top:52px}
.social{display:flex;justify-content:center;gap:22px;margin-top:30px}
.social span{width:78px;height:78px;border-radius:50%;background:rgba(255,255,255,.25)}

/* footer */
.site-footer{position:absolute;top:2748px;left:0;width:1200px;height:339px}
.foot-col{position:absolute;top:68px}
.foot-col h4{font-size:15px;font-weight:600;text-transform:uppercase;letter-spacing:.5px;margin-bottom:32px}
.contact{left:39px}
.hours{left:420px}
.reserve{left:800px}
.foot-line{display:flex;gap:16px;font-size:14px;line-height:1.45;margin-bottom:16px}
.foot-line svg{flex:none;margin-top:2px}
.hours .foot-line b{font-weight:600}
.reserve .btn{width:136px;height:47px;line-height:49px;margin-top:-8px}
.copyright{position:absolute;left:0;width:1200px;top:300px;text-align:center;font-size:11px;text-transform:uppercase;letter-spacing:.8px;border-top:1px solid rgba(0,0,0,.08);padding-top:12px}
</style>
</head>
<body>

<header class="site-header">
  <a class="brand" href="#"><span class="brand-dot"></span>Liora</a>
  <nav class="main-nav">
    <a class="active" href="#">Homepage</a>
    <a href="#">Menu</a>
    <a href="#">Location</a>
    <a href="#">Events</a>
    <a href="#">Delivery</a>
    <a href="#">Join Team</a>
  </nav>
  <a class="btn btn-book" href="#">Book a Table</a>
</header>

<section class="hero">
  <div class="hero-photo" role="img" aria-label="Plate of pesto tagliatelle topped with parmesan and parsley"></div>
  <div class="hero-copy">
    <div class="hero-rule"></div>
    <h1 class="hero-title">Get Your Flavors Of</h1>
    <div class="hero-script">Mediterranean</div>
    <div class="hero-price">FROM <b>10$</b></div>
    <div class="hero-rule"></div>
  </div>
  <a class="btn" href="#">View Menu</a>
  <div class="slider-dots"><span class="on"></span><span></span><span></span></div>
</section>

<section class="menu-cards">
  <article class="menu-card">
    <div class="photo" role="img" aria-label="Shakshuka pan with eggs, bread and coffee" style="background:linear-gradient(135deg,#8b7b6a,#d9623a 50%,#6f6258)"></div>
    <h3>Breakfast</h3>
    <div class="price">From <b>10$</b></div>
    <a class="btn" href="#">View Menu</a>
  </article>
  <article class="menu-card">
    <div class="photo" role="img" aria-label="Creamy pasta with chicken and parsley" style="background:radial-gradient(circle at 50% 55%,#c9935a,#e9ddc9 60%,#f3f0ea)"></div>
    <h3>Pasta</h3>
    <div class="price">From <b>14$</b></div>
    <a class="btn" href="#">View Menu</a>
  </article>
  <article class="menu-card">
    <div class="photo" role="img" aria-label="Stuffed pita sandwich with fries and salad" style="background:linear-gradient(135deg,#d9a441,#c98b52 45%,#6e8f3c 80%,#d14a3a)"></div>
    <h3>Mains</h3>
    <div class="price">From <b>24$</b></div>
    <a class="btn" href="#">View Menu</a>
  </article>
</section>

<section class="ingredients" role="img" aria-label="Fresh salmon fillet with olive oil, basil, tomato, chili and sea salt on slate">
  <div class="script">Ingredients</div>
  <h2>FRESH AND HEALTHY</h2>
  <p>Our creative Mediterranean cuisine combines fresh products, a subtle blend of spices and exotic flavors</p>
  <a class="btn" href="#">View Menu</a>
</section>

<section class="story">
  <div class="story-photo marina" role="img" aria-label="Glass of white wine on a table by the marina"></div>
  <div class="story-photo lounge" role="img" aria-label="Café lounge with arched tiled alcoves and red cushions"></div>
  <div class="story-text">
    <div class="script">How It Began</div>
    <h2>OUR STORY</h2>
    <p>A slow morning walk to the bakery around the corner is a way of life by the sea. Nothing beats the first warm loaf of the day. Our café began with one simple idea: we wanted guests to enjoy food that tastes good every time. So we paired the finest ingredients with honest recipes, from warm stuffed pita to fresh salads, made just the way you like whenever the craving calls.</p>
    <p>As time went by we opened our hearts and doors to our guests and added a range of fresh and delicious dishes to our menu - salads, classic starters, desserts and we made sure you never miss out on a great morning latte.</p>
  </div>
</section>

<section class="follow">
  <h2>FOLLOW US</h2>
  <div class="social">
    <span role="img" aria-label="Social network link"></span>
    <span role="img" aria-label="Social network link"></span>
    <span role="img" aria-label="Social network link"></span>
    <span role="img" aria-label="Review site link"></span>
  </div>
</section>

<footer class="site-footer">
  <div class="foot-col contact">
    <h4>Contact</h4>
    <div class="foot-line">
      <svg width="12" height="16" viewBox="0 0 12 16"><path d="M6 0a6 6 0 0 1 6 6c0 4-6 10-6 10S0 10 0 6a6 6 0 0 1 6-6z" fill="#f23d3b"/><circle cx="6" cy="6" r="2.2" fill="#f8eed6"/></svg>
      <span>14 Harbour Lane | Seaview Point, Singapore<br>000000, Singapore</span>
    </div>
    <div class="foot-line">
      <svg width="14" height="14" viewBox="0 0 14 14"><path d="M3 0l3 3-2 2c1 2 3 4 5 5l2-2 3 3-2 3C6 14 0 8 0 3z" fill="#f23d3b"/></svg>
      <span>6100 0000</span>
    </div>
    <div class="foot-line">
      <svg width="14" height="11" viewBox="0 0 14 11"><rect width="14" height="11" fill="#f23d3b"/><path d="M0 0l7 6 7-6" fill="none" stroke="#f8eed6" stroke-width="1.4"/></svg>
      <span>info@lioracafe.com<br>or reservations@lioracafe.com</span>
    </div>
  </div>
  <div class="foot-col hours">
    <h4>Opening Hours</h4>
    <div class="foot-line">
      <svg width="14" height="14" viewBox="0 0 14 14"><circle cx="7" cy="7" r="6" fill="none" stroke="#f23d3b" stroke-width="1.6"/><path d="M7 3.5V7h3" fill="none" stroke="#f23d3b" stroke-width="1.6"/></svg>
      <span><b>Monday- Thursday - Friday</b><br>8:30 - 3pm and 5:30pm till 10pm<br><b>Tuesday- Saturday - Sunday</b><br>and public holiday 8am till 10pm<br><b>Wednesday</b> -Close</span>
    </div>
  </div>
  <div class="foot-col reserve">
    <h4>Make Reservation</h4>
    <a class="btn" href="#">Book a Table</a>
  </div>
  <div class="copyright">Liora Cafe © 2015. All rights reserved.</div>
</footer>

</body>
</html>
```